Serious, Modern Hard Rock CD Cover design for Montana Band

We need a CD Cover for a Montana rock band. We come out of a city of about 40k people nestled in the mountains. We are probably the only hard rock band in our city, so we are trying to cater to a broader sound that isn't TOO heavy but also still trying to stay unique.

We are going to do a front and back CD cover (the CD will be a paper jacket/sleeve).

As for stylistic choices, I'd love a landscape style, modern cover. Some sort of edited picture of mountains, sidewalks, city, forest, highway, anything with a somber/ambient/serious feel. It can even be rendered, something like clouds?

If you could include our name written in a modern/eye popping way AND/OR a modern, geometric logo, and make it work, that'd be awesome. We need some sort of takeaway logo on the album that we could use for the future. We just need something to put on drum heads, stickers, etc in the future. Doesn't need to be crazy, maybe just a couple lines or circles.

What I am imagining is a mysterious/somber background with colorful accents on either on the background image or the logo.

I've attached some cool covers I've seen on this site and one I made myself to hopefully understand what I'm going for.

Our band name is Nine Step Lantern, with the Five spelled out. Name of the album is You and Kerosene.

The tracks on the back are as follows:

Soft Heel
You and Kerosene
Baron's Field
Ashes
RVN
Double Knot

Logo Text

Nine Step Lantern

Colors

Designer to choose colors to be used in the design.

Requirements
Must have
• Some sort of takeaway logo that we could use for the future (our name in a cool font, some cool geometric logo).
Nice to have
• A logo or art of some sort that we can continue to use
• Drier colors
• Landscapes
• Sidewalk
• Mountains
• Forest
• Grunge
• Anything!
Should not have
• Any image pertaining to Gasoline (the album name)

```html
<!DOCTYPE html>
<html lang="en">
<head>
<meta charset="utf-8">
<title>Nine Step Lantern – You and Kerosene – CD Sleeve</title>
<link rel="stylesheet" href="https://fonts.googleapis.com/css2?family=Oswald:wght@400;500&family=Questrial&family=Arimo:wght@700&display=swap">
<style>
  :root {
    --backdrop: #d6d8d5;
    --sky-rose: #c88c86;
    --sky-lilac: #aba2ba;
    --sky-haze: #bdbac8;
    --hill: #4a4f52;
    --road: #5a5c5e;
    --road-dark: #3c3e40;
    --ink-white: #f4f2f2;
    --ink-dark: #2a2a30;
    --accent-red: #d2564f;
    --badge: #2b2c2e;
  }
  * { margin: 0; padding: 0; box-sizing: border-box; }
  html, body { width: 1200px; height: 876px; overflow: hidden; }
  body { background: var(--backdrop); position: relative; }

  .sleeve { position: absolute; overflow: hidden; }
  .sleeve--back { left: 16px; top: 230px; width: 502px; height: 502px; }
  .sleeve--front { left: 552px; top: 155px; width: 636px; height: 637px; }

  .scenery { position: absolute; inset: 0; }
  .sleeve--back .scenery {
    background: linear-gradient(180deg, var(--sky-rose) 0%, var(--sky-lilac) 20%, var(--sky-haze) 38%,
      #8d8c94 46%, #6f6a66 54%, #8a8b8c 62%, var(--road) 76%, var(--road-dark) 100%);
  }
  .sleeve--front .scenery {
    background: linear-gradient(180deg, var(--sky-rose) 0%, var(--sky-lilac) 20%, var(--sky-haze) 40%,
      #8f95a0 44%, var(--hill) 50%, #707274 56%, var(--road) 66%, var(--road-dark) 100%);
  }

  .frame {
    position: absolute; left: 26px; top: 30px; width: 464px; height: 444px;
    border: 2px solid var(--ink-white);
  }
  .frame__header {
    height: 38px; border-bottom: 2px solid var(--ink-white);
    display: flex; align-items: center; justify-content: center; gap: 6px;
    font-family: "Oswald", sans-serif; font-weight: 400; font-size: 19px;
    color: var(--ink-white); letter-spacing: 0.2px;
  }
  .frame__header .dot { color: var(--accent-red); font-size: 14px; }

  .tracklist {
    list-style: none; margin-top: 2px; text-align: center;
    font-family: "Arimo", sans-serif; font-weight: 700; font-size: 15px;
    color: var(--ink-dark); line-height: 24px;
  }
  .tracklist .num { font-size: 11px; font-weight: 700; margin-right: 3px; }
  .tracklist .track { margin: 0 4px; }

  .back-mark {
    position: absolute; left: 206px; top: 332px; width: 90px;
    font-family: "Oswald", sans-serif; font-weight: 400; font-size: 17px; line-height: 22px;
    color: var(--ink-white); text-align: center; letter-spacing: 1px;
  }

  .credit {
    position: absolute; left: 3px; top: 470px; transform-origin: left top; transform: rotate(-90deg);
    font-family: "Oswald", sans-serif; font-size: 7px; color: var(--ink-white); opacity: 0.75;
    letter-spacing: 0.4px; white-space: nowrap;
  }

  .album-title {
    position: absolute; left: 26px; top: 200px; transform-origin: left top; transform: rotate(-90deg);
    font-family: "Oswald", sans-serif; font-weight: 500; font-size: 21px;
    color: var(--ink-white); letter-spacing: 0.3px; white-space: nowrap;
  }

  .band-badge {
    position: absolute; left: 338px; top: 337px; width: 270px; height: 270px; border-radius: 50%;
    background: var(--badge);
    display: flex; flex-direction: column; align-items: center; justify-content: center;
    padding-bottom: 22px;
    font-family: "Questrial", sans-serif; font-size: 31px; line-height: 42px;
    color: var(--ink-white); letter-spacing: 1.5px; text-align: center;
  }
</style>
</head>
<body>
  <section class="sleeve sleeve--back" aria-label="Back cover">
    <div class="scenery" role="img" aria-label="Photo of a coastal highway with an orange centre line curving past a concrete arch bridge under a dusky pink and lilac sky"></div>
    <div class="frame">
      <h2 class="frame__header">NINE STEP LANTERN <span class="dot">•</span> YOU AND KEROSENE</h2>
      <ul class="tracklist">
        <li><span class="track"><span class="num">1.</span>SOFT HEEL</span> <span class="track"><span class="num">2.</span>YOU AND KEROSENE</span></li>
        <li><span class="track"><span class="num">3.</span>BARON'S FIELD</span> <span class="track"><span class="num">4.</span>ASHES</span></li>
        <li><span class="track"><span class="num">5.</span>RVN</span> <span class="track"><span class="num">6.</span>DOUBLE KNOT</span></li>
      </ul>
    </div>
    <p class="back-mark">NINE<br>STEP<br>LANTERN</p>
    <p class="credit">2024 NINE STEP LANTERN ALL RIGHTS RESERVED</p>
  </section>

  <section class="sleeve sleeve--front" aria-label="Front cover">
    <div class="scenery" role="img" aria-label="Photo of an empty highway with an orange centre line curving along a guardrail toward dark mountains and a lake under a pink and lilac sky"></div>
    <h1 class="album-title">YOU AND KEROSENE</h1>
    <div class="band-badge"><span>NINE STEP</span><span>LANTERN</span></div>
  </section>
</body>
</html>
```